Heavy Duty Repairs Poster

Good afternoon - I'm looking for a poster , design to set up around different areas. The Poster must consist of the following
- Heavy duty repairs
- Pictures of Semi trucks , heavy construction equipment , trailers
- Agriculture
- All north American equipment ( see attached pictures)
- Brief Descriptions in bullet point forms
CVIPS
WELDING
AIR CONDITIONING
ENGINE REBUILDS
DIAGONSTICS
FLEET MANAGMENT
TIRE REPAIR AND SALES
ELECTRICAL , HYDRALIC , POWER TRAIN SERVICE AND REPAIRS
PART SALES
FLEET MAINTINACE
DELTEING AND TUNING
AFTER MARKET INSTALLS OUTFITTING
ONSITE & OFFSITE REPAIRS
FULL RECERTIFACTION OVERHAULING
Warranty Approved

Target Market(s)

Heavy Duty Truck , Equipment , Agriculture Owners

Industry/Entity Type

Heavy Duty Repairs

Colors
EB3D1F
EC4F4E
F09395
F8D3D4
FCEDEE

Requirements
Must have
• Pictures of : Semi trucks and trailer , Construction heavy equipment , agriculture equipment
Nice to have
• Flashy and stands out

```html
<!DOCTYPE html>
<html lang="en">
<head>
<meta charset="utf-8">
<title>Heavy Duty Repairs Poster</title>
<link rel="stylesheet" href="https://fonts.googleapis.com/css2?family=Bebas+Neue&family=Montserrat:wght@400;600;700&family=Archivo+Black&display=swap">
<style>
  :root {
    --page: #ffffff;
    --ink-white: #ffffff;
    --band-black: #000000;
    --red-deep: #8e0a10;
    --red: #d4141c;
    --red-bright: #eb3d1f;
    --pink: #ec4f4e;
    --pink-soft: #f09395;
    --violet: #5a1466;
    --magenta: #c8308a;
    --phone-red: #e0141c;
    --truck-red: #b0121a;
    --trailer-grey: #d9c9cc;
  }
  html, body {
    margin: 0;
    padding: 0;
    width: 1200px;
    height: 1200px;
    overflow: hidden;
    background: var(--page);
  }
  .canvas {
    position: relative;
    width: 1200px;
    height: 1200px;
    background: var(--page);
  }
  .poster {
    position: absolute;
    left: 228px;
    top: 39px;
    width: 751px;
    height: 1136px;
    overflow: hidden;
    font-family: "Montserrat", sans-serif;
    color: var(--ink-white);
  }
  .hero-photo {
    position: absolute;
    left: 0;
    top: 0;
    width: 751px;
    height: 896px;
    background:
      radial-gradient(ellipse 420px 180px at 560px 230px, rgba(255,170,150,0.55), transparent 70%),
      linear-gradient(180deg, var(--violet) 0%, var(--magenta) 14%, var(--pink) 26%, var(--red) 42%, var(--red) 62%, var(--red-deep) 100%);
  }
  .truck-photo {
    position: absolute;
    left: 41px;
    top: 150px;
    width: 362px;
    height: 280px;
    border-radius: 18px;
    background:
      radial-gradient(ellipse 140px 110px at 110px 170px, rgba(40,8,10,0.55), transparent 75%),
      linear-gradient(100deg, var(--truck-red) 0%, var(--truck-red) 45%, var(--trailer-grey) 75%, rgba(217,201,204,0.4) 100%);
    opacity: 0.85;
  }
  .headline {
    position: absolute;
    left: 322px;
    top: 87px;
    width: 400px;
    margin: 0;
    text-align: center;
    font-family: "Bebas Neue", sans-serif;
    font-weight: 400;
    font-size: 180px;
    line-height: 131px;
    letter-spacing: -4px;
    color: var(--ink-white);
  }
  .headline span { display: block; }
  .headline .word-heavy { transform: scaleX(0.86); }
  .headline .word-duty { transform: scaleX(0.8); }
  .headline .word-repairs { transform: scaleX(0.9); }
  .service-list {
    position: absolute;
    top: 503px;
    margin: 0;
    padding: 0;
    list-style: none;
    font-size: 17.5px;
    font-weight: 400;
    line-height: 22.5px;
    letter-spacing: 0.2px;
  }
  .service-list.left { left: 78px; width: 290px; }
  .service-list.right { left: 425px; width: 300px; }
  .service-list li {
    position: relative;
    padding-left: 24px;
    margin-bottom: 9.1px;
  }
  .service-list .tick {
    position: absolute;
    left: 0;
    top: 3px;
    width: 17px;
    height: 16px;
  }
  .warranty-seal {
    position: absolute;
    left: 549px;
    top: 750px;
    width: 140px;
    height: 140px;
  }
  .seal-arc { font-family: "Archivo Black", sans-serif; font-size: 19px; letter-spacing: 1px; fill: var(--ink-white); }
  .seal-word { font-family: "Montserrat", sans-serif; font-weight: 700; font-size: 13px; fill: var(--ink-white); }
  .brand-band {
    position: absolute;
    left: 0;
    top: 896px;
    width: 751px;
    height: 240px;
    background: var(--band-black);
    text-align: center;
  }
  .brand-name {
    position: absolute;
    left: 0;
    right: 0;
    top: 108px;
    margin: 0;
    font-family: "Montserrat", sans-serif;
    font-weight: 600;
    font-size: 22px;
    color: var(--ink-white);
  }
  .brand-location {
    position: absolute;
    left: 0;
    right: 0;
    top: 144px;
    margin: 0;
    font-family: "Montserrat", sans-serif;
    font-weight: 600;
    font-size: 17px;
    color: var(--ink-white);
  }
  .phone {
    position: absolute;
    left: 0;
    right: 0;
    top: 170px;
    margin: 0;
    font-family: "Archivo Black", sans-serif;
    font-size: 64px;
    line-height: 70px;
    letter-spacing: 0.5px;
    color: var(--phone-red);
  }
</style>
</head>
<body>
<div class="canvas">
  <article class="poster">
    <div class="hero-photo" role="img" aria-label="Highway at a pink and purple sunset sky, trees along the road"></div>
    <div class="truck-photo" role="img" aria-label="Photo of a red semi truck pulling a white trailer on the highway"></div>

    <h1 class="headline">
      <span class="word-heavy">Heavy</span>
      <span class="word-duty">Duty</span>
      <span class="word-repairs">Repairs</span>
    </h1>

    <ul class="service-list left">
      <li><svg class="tick" viewBox="0 0 17 16"><path d="M1 9 L6 14 L16 1" fill="none" stroke="#fff" stroke-width="3" stroke-linecap="round" stroke-linejoin="round"/></svg>CVIPS</li>
      <li><svg class="tick" viewBox="0 0 17 16"><path d="M1 9 L6 14 L16 1" fill="none" stroke="#fff" stroke-width="3" stroke-linecap="round" stroke-linejoin="round"/></svg>WELDING</li>
      <li><svg class="tick" viewBox="0 0 17 16"><path d="M1 9 L6 14 L16 1" fill="none" stroke="#fff" stroke-width="3" stroke-linecap="round" stroke-linejoin="round"/></svg>AIR CONDITIONING</li>
      <li><svg class="tick" viewBox="0 0 17 16"><path d="M1 9 L6 14 L16 1" fill="none" stroke="#fff" stroke-width="3" stroke-linecap="round" stroke-linejoin="round"/></svg>ENGINE REBUILDS</li>
      <li><svg class="tick" viewBox="0 0 17 16"><path d="M1 9 L6 14 L16 1" fill="none" stroke="#fff" stroke-width="3" stroke-linecap="round" stroke-linejoin="round"/></svg>DIAGONSTICS</li>
      <li><svg class="tick" viewBox="0 0 17 16"><path d="M1 9 L6 14 L16 1" fill="none" stroke="#fff" stroke-width="3" stroke-linecap="round" stroke-linejoin="round"/></svg>FLEET MANAGMENT</li>
      <li><svg class="tick" viewBox="0 0 17 16"><path d="M1 9 L6 14 L16 1" fill="none" stroke="#fff" stroke-width="3" stroke-linecap="round" stroke-linejoin="round"/></svg>TIRE REPAIR AND SALES</li>
      <li><svg class="tick" viewBox="0 0 17 16"><path d="M1 9 L6 14 L16 1" fill="none" stroke="#fff" stroke-width="3" stroke-linecap="round" stroke-linejoin="round"/></svg>ELECTRICAL , HYDRALIC , POWER TRAIN SERVICE AND REPAIRS</li>
    </ul>

    <ul class="service-list right">
      <li><svg class="tick" viewBox="0 0 17 16"><path d="M1 9 L6 14 L16 1" fill="none" stroke="#fff" stroke-width="3" stroke-linecap="round" stroke-linejoin="round"/></svg>PART SALES</li>
      <li><svg class="tick" viewBox="0 0 17 16"><path d="M1 9 L6 14 L16 1" fill="none" stroke="#fff" stroke-width="3" stroke-linecap="round" stroke-linejoin="round"/></svg>FLEET MAINTINACE</li>
      <li><svg class="tick" viewBox="0 0 17 16"><path d="M1 9 L6 14 L16 1" fill="none" stroke="#fff" stroke-width="3" stroke-linecap="round" stroke-linejoin="round"/></svg>DELTEING AND TUNING</li>
      <li><svg class="tick" viewBox="0 0 17 16"><path d="M1 9 L6 14 L16 1" fill="none" stroke="#fff" stroke-width="3" stroke-linecap="round" stroke-linejoin="round"/></svg>AFTER MARKET INSTALLS</li>
      <li><svg class="tick" viewBox="0 0 17 16"><path d="M1 9 L6 14 L16 1" fill="none" stroke="#fff" stroke-width="3" stroke-linecap="round" stroke-linejoin="round"/></svg>OUTFITTING</li>
      <li><svg class="tick" viewBox="0 0 17 16"><path d="M1 9 L6 14 L16 1" fill="none" stroke="#fff" stroke-width="3" stroke-linecap="round" stroke-linejoin="round"/></svg>ONSITE &amp; OFFSITE REPAIRS</li>
      <li><svg class="tick" viewBox="0 0 17 16"><path d="M1 9 L6 14 L16 1" fill="none" stroke="#fff" stroke-width="3" stroke-linecap="round" stroke-linejoin="round"/></svg>FULL RECERTIFACTION</li>
      <li><svg class="tick" viewBox="0 0 17 16"><path d="M1 9 L6 14 L16 1" fill="none" stroke="#fff" stroke-width="3" stroke-linecap="round" stroke-linejoin="round"/></svg>OVERHAULING</li>
    </ul>

    <svg class="warranty-seal" viewBox="0 0 140 140" role="img" aria-label="Warranty approved seal">
      <defs>
        <path id="seal-top-arc" d="M 20 70 A 50 50 0 0 1 120 70"/>
        <polygon id="seal-star" points="0,-5 1.2,-1.6 4.8,-1.6 1.9,0.6 3,4 0,2 -3,4 -1.9,0.6 -4.8,-1.6 -1.2,-1.6" fill="#fff"/>
      </defs>
      <circle cx="70" cy="70" r="68" fill="none" stroke="#fff" stroke-width="1.2"/>
      <circle cx="70" cy="70" r="42" fill="none" stroke="#fff" stroke-width="1.2"/>
      <text class="seal-arc"><textPath href="#seal-top-arc" startOffset="50%" text-anchor="middle">WARRANTY</textPath></text>
      <text class="seal-word" x="70" y="75" text-anchor="middle">APPROVED</text>
      <use href="#seal-star" x="14" y="69"/>
      <use href="#seal-star" x="126" y="69"/>
      <use href="#seal-star" x="20" y="95"/>
      <use href="#seal-star" x="120" y="95"/>
      <use href="#seal-star" x="35" y="115"/>
      <use href="#seal-star" x="105" y="115"/>
      <use href="#seal-star" x="70" y="125"/>
    </svg>

    <footer class="brand-band">
      <p class="brand-name">Ridgeline Mechanical Services</p>
      <p class="brand-location">Pinecrest , Alberta</p>
      <p class="phone">780-555-0147</p>
    </footer>
  </article>
</div>
</body>
</html>
```